Cloud backup company needs a new website

We need a new design for our website as the current one is quite dated now. You can view the current website at www.vellostrand-files.net.au to view the content elements.

We provide cloud backup services (ie remote off site to a cluster of servers) to small to medium businesses looking for better alternatives to tape or optical media backups.

Target Market(s)

SME/SMB (Businesses with fewer than 100 employees)

Industry/Entity Type

It Company

Requirements
Must have
• Must have sections to sign up to newsletter, log in to account, view news feed as per current website.

Must have a prominent call to action to sign up for a trial and view pricing.

Also like it to have twitter and facebook links/likes integration
Should not have
• No Flash, no serif fonts

```html
<!DOCTYPE html>
<html lang="en">
<head>
<meta charset="utf-8">
<title>Vellostrand – Cloud Backup</title>
<link href="https://fonts.googleapis.com/css2?family=Source+Sans+3:wght@400;600&family=Oswald:wght@300;400&display=swap" rel="stylesheet">
<style>
:root{
  --orange:#e4662c;
  --orange-light:#f08a4b;
  --dark:#3b3b3c;
  --mid:#6b6b6d;
  --header:#e6e6e8;
  --text:#4a4a4a;
  --line:#d8d8d8;
  --white:#ffffff;
}
*{box-sizing:border-box;margin:0;padding:0}
html,body{width:1200px;height:1182px;overflow:hidden}
body{position:relative;background:var(--white);font-family:"Source Sans 3",Arial,sans-serif;color:var(--text)}
.abs{position:absolute}
.condensed{font-family:"Oswald","Arial Narrow",sans-serif}

.top-bar{left:0;top:0;width:1200px;height:23px;background:var(--dark);color:#eee}
.top-bar .phone{left:823px;top:0;height:23px;display:flex;align-items:center;gap:6px;font-family:"Oswald",sans-serif;font-weight:300;font-size:20px}
.top-bar .contact{left:966px;top:0;height:23px;display:flex;align-items:center;gap:6px;font-size:12px}

.header{left:0;top:23px;width:1200px;height:58px;background:var(--header)}
.logo{left:154px;top:8px;display:flex;align-items:center;gap:8px;font-size:34px;font-weight:600;color:var(--orange);letter-spacing:-0.5px}
.logo .dot{width:14px;height:14px;border-radius:50%;background:var(--orange)}
.search{left:904px;top:16px;width:133px;height:30px;background:var(--white);border:1px solid #cfcfcf;font-size:11px;color:#666;padding:8px 10px}
.search svg{position:absolute;right:8px;top:6px}

.main-nav{left:0;top:81px;width:1200px;height:26px;background:linear-gradient(#5a5a5b,#2f2f30);border-top:1px solid #777}
.main-nav a{position:absolute;top:0;height:25px;line-height:25px;font-size:11px;color:#f2f2f2;text-decoration:none;text-align:center;border-right:1px solid #1f1f1f}
.main-nav a.last{border-right:none}

.hero-band{left:0;top:107px;width:1200px;height:420px;background:var(--header)}
.slider{left:155px;top:2px;width:883px;height:400px;background:radial-gradient(ellipse at 30% 40%,#d8c1ad 0%,#b89a84 40%,#5b4a40 75%,#2b2420 100%);box-shadow:0 2px 4px rgba(0,0,0,.45);border:2px solid #fff}
.slide-arrow{top:176px;width:44px;height:44px;border-radius:50%;background:#6c6c6c;border:3px solid #5a5a5a;display:flex;align-items:center;justify-content:center}
.slide-arrow span{width:26px;height:26px;border-radius:50%;background:#eee;display:flex;align-items:center;justify-content:center}
.login{left:598px;top:9px;width:272px;height:122px;background:rgba(25,22,20,.85);color:#eee}
.login h2{position:absolute;left:16px;top:11px;font-family:"Oswald",sans-serif;font-weight:300;font-size:17px;letter-spacing:.2px}
.login .field{position:absolute;top:44px;width:124px;height:22px;background:var(--white);color:#666;font-size:11px;padding:4px 7px}
.login .links{position:absolute;left:17px;top:82px;font-size:11px;line-height:15px}
.login .btn{position:absolute;left:219px;top:73px;width:48px;height:24px;background:var(--orange);color:#fff;font-size:13px;text-align:center;line-height:23px}

.section-title{font-size:18px;color:var(--orange);font-weight:400}

.steps{left:152px;top:568px;width:540px;height:129px;border:1px solid var(--line);background:linear-gradient(#fff,#ececec);display:flex}
.step{position:relative;border-right:1px solid var(--line);text-align:center}
.step:last-child{border-right:none}
.step .icon{position:absolute;top:24px;width:44px;height:44px;border-radius:50%;background:var(--orange);display:flex;align-items:center;justify-content:center;box-shadow:0 1px 2px rgba(0,0,0,.25)}
.step .label{position:absolute;top:74px;width:100%;font-size:18px;color:#444}

.afford-panel{left:152px;top:744px;width:525px;height:265px;background:var(--mid);color:#f0f0f0;padding:18px 22px;font-size:12.5px;line-height:21px}
.afford-panel p{margin-bottom:12px}
.btn-orange{position:absolute;background:linear-gradient(var(--orange-light),var(--orange));color:#fff;font-family:"Oswald",sans-serif;font-weight:300;text-align:center;box-shadow:0 2px 3px rgba(0,0,0,.3);border-radius:3px}

.news{left:719px;top:568px;width:316px;height:203px;border:1px solid var(--line);background:linear-gradient(#fff,#ededed)}
.news-item{position:absolute;left:12px;width:292px;padding-left:38px}
.news-item .bullet{position:absolute;left:10px;top:3px;width:12px;height:12px;border-radius:50%;border:1px solid #aaa;background:#fafafa}
.news-item h3{font-size:14px;font-weight:400;color:#333;margin-bottom:4px}
.news-item p{font-size:12px;line-height:18.5px;color:#555}
.news-item a{font-size:12px;color:var(--orange);text-decoration:none}
.pager{top:541px;width:13px;height:13px;border-radius:50%;border:1px solid #aaa;background:#f4f4f4}

.nl-field{left:719px;width:316px;height:31px;background:linear-gradient(#f6f6f6,#ececec);border:1px solid #e0e0e0;font-size:12px;color:#555;padding:7px 14px}

.footer{left:0;top:1031px;width:1200px;height:151px;background:linear-gradient(#6a6a6c,#5a5a5c);color:#eee}
.footer .follow{left:154px;top:30px;font-size:12.5px}
.social{top:58px;width:23px;height:23px;border-radius:3px}
.footer .legal{left:154px;top:102px;font-size:11px;line-height:22px}
.footer .links{right:162px;top:104px;font-size:11px}
.badges{left:793px;top:15px;width:246px;height:65px;background:var(--white)}
</style>
</head>
<body>

<div class="abs top-bar">
  <div class="abs phone">
    <svg width="14" height="16" viewBox="0 0 14 16"><rect x="1" y="1" width="12" height="14" rx="2" fill="none" stroke="#eee" stroke-width="1.6"/><rect x="4" y="4" width="6" height="3" fill="#eee"/><rect x="4" y="9" width="2" height="2" fill="#eee"/><rect x="8" y="9" width="2" height="2" fill="#eee"/></svg>
    1300 555 019
  </div>
  <div class="abs contact">
    <svg width="16" height="11" viewBox="0 0 16 11"><rect x="0.5" y="0.5" width="15" height="10" fill="#eee"/><path d="M1 1l7 5 7-5" fill="none" stroke="#3b3b3c" stroke-width="1.3"/></svg>
    Contact Us
  </div>
</div>

<header class="abs header">
  <div class="abs logo"><span class="dot"></span>vellostrand</div>
  <div class="abs search">Search
    <svg width="18" height="18" viewBox="0 0 18 18"><circle cx="7" cy="7" r="5" fill="#cfe3f5" stroke="#5a8fc4" stroke-width="1.8"/><path d="M11 11l5 5" stroke="#e08a2c" stroke-width="3" stroke-linecap="round"/></svg>
  </div>
</header>

<nav class="abs main-nav">
  <a style="left:154px;width:120px">HOME</a>
  <a style="left:274px;width:119px">SOLUTIONS</a>
  <a style="left:393px;width:121px">SERVICES</a>
  <a style="left:514px;width:125px">SUPPORT</a>
  <a style="left:639px;width:137px">PARTNERS</a>
  <a style="left:776px;width:135px">ABOUT</a>
  <a class="last" style="left:911px;width:132px">DOWNLOAD</a>
</nav>

<section class="abs hero-band">
  <div class="abs slider" role="img" aria-label="Close-up photo of an open hard disk drive with platter and read arm">
    <div class="abs slide-arrow" style="left:14px">
      <span><svg width="12" height="10" viewBox="0 0 12 10"><path d="M6 0L1 5l5 5zM11 0L6 5l5 5z" fill="#444"/></svg></span>
    </div>
    <div class="abs slide-arrow" style="left:815px">
      <span><svg width="12" height="10" viewBox="0 0 12 10"><path d="M1 0l5 5-5 5zM6 0l5 5-5 5z" fill="#444"/></svg></span>
    </div>
    <div class="abs login">
      <h2>LOG IN TO ACCOUNT</h2>
      <div class="field" style="left:16px">user name</div>
      <div class="field" style="left:144px">password</div>
      <div class="links">Create new account<br>Register &nbsp;&nbsp;|&nbsp;&nbsp; Forgot Password?</div>
      <div class="btn">Login</div>
    </div>
  </div>
</section>

<h2 class="abs section-title" style="left:151px;top:537px">How Vellostrand Works</h2>
<div class="abs steps">
  <div class="step" style="width:97px">
    <div class="icon" style="left:27px"><svg width="22" height="22" viewBox="0 0 22 22"><path d="M11 3l-6 6h4v6h4V9h4z" fill="#fff"/><path d="M3 14v5h16v-5" fill="none" stroke="#fff" stroke-width="2.2"/></svg></div>
    <div class="label">Install</div>
  </div>
  <div class="step" style="width:148px">
    <div class="icon" style="left:52px"><svg width="22" height="22" viewBox="0 0 22 22"><ellipse cx="10" cy="5" rx="7" ry="3" fill="#fff"/><path d="M3 8c0 2 14 2 14 0v3c0 2-14 2-14 0zM3 13c0 2 14 2 14 0v3c0 2-14 2-14 0z" fill="#fff"/><circle cx="16" cy="16" r="4" fill="#fff" stroke="#e4662c" stroke-width="1.5"/></svg></div>
    <div class="label">Create Backup</div>
  </div>
  <div class="step" style="width:162px">
    <div class="icon" style="left:59px"><svg width="22" height="22" viewBox="0 0 22 22"><rect x="3" y="5" width="13" height="13" rx="2" fill="none" stroke="#fff" stroke-width="2"/><path d="M9 13l9-9 2 2-9 9-3 1z" fill="#fff"/></svg></div>
    <div class="label">Schedule Backup</div>
  </div>
  <div class="step" style="width:131px">
    <div class="icon" style="left:18px"><svg width="24" height="24" viewBox="0 0 24 24"><path d="M5 12a7 7 0 0 1 12-5l-3 1 6 3 0-6-2 2A9 9 0 0 0 3 12z" fill="#fff"/><path d="M19 12a7 7 0 0 1-12 5l3-1-6-3 0 6 2-2a9 9 0 0 0 15-5z" fill="#fff"/></svg></div>
    <div class="label" style="text-align:left;padding-left:13px;top:76px">Restore<div class="condensed" style="font-size:12px;font-weight:400;margin-top:-2px">IT REALLY IS THAT SIMPLE</div></div>
  </div>
</div>

<h2 class="abs section-title" style="left:151px;top:713px">How much could you afford to lose?</h2>
<div class="abs afford-panel">
  <p>Most companies believe their critical data is adequately protected from a catastrophic event – until something happens. Is this really how you plan to determine whether or not your business continuity management or disaster recovery plan is 100% effective?</p>
  <p>For the Small to Medium Business Enterprise (SME), any event that wipes out all information could easily be the end of that business. As a result, no business can afford to cut corners when it comes to protecting their data from any unforeseen event.</p>
  <p>Offsite Backup is a fundamental disaster recovery requirement of any sized business or any professional in a sole practice that uses computers to store information.</p>
  <div class="btn-orange" style="left:20px;top:219px;width:148px;height:33px;line-height:33px;font-size:15px">DOWNLOAD TRIAL NOW</div>
</div>

<h2 class="abs section-title" style="left:719px;top:537px">News</h2>
<div class="abs pager" style="left:1006px"></div>
<div class="abs pager" style="left:1024px"></div>
<div class="abs news">
  <div class="news-item" style="top:20px">
    <span class="bullet"></span>
    <h3>Are You Ready for Your Server to Fail?</h3>
    <p>What would you do if you walked into your office tomorrow morning, switched on your ...</p>
    <a>READ MORE &gt;&gt;</a>
  </div>
  <div style="position:absolute;left:12px;top:101px;width:292px;border-top:1px solid var(--line)"></div>
  <div class="news-item" style="top:111px">
    <span class="bullet"></span>
    <h3>Remote, Offsite Backup a Great Value</h3>
    <p>The idea of sending mission critical data over the Internet was a scary proposition for ...</p>
    <a>READ MORE &gt;&gt;</a>
  </div>
</div>

<h2 class="abs section-title" style="left:719px;top:792px">Newsletter Signup</h2>
<div class="abs nl-field" style="top:823px">Enter the Name</div>
<div class="abs nl-field" style="top:860px">Enter the E mail id</div>
<div class="btn-orange" style="left:961px;top:899px;width:74px;height:33px;line-height:33px;font-size:15px">SUBSCRIBE</div>
<div class="btn-orange" style="left:871px;top:975px;width:163px;height:33px;line-height:33px;font-size:20px;text-align:left">
  <span style="display:inline-block;width:36px;height:33px;vertical-align:top;border-right:1px solid rgba(255,255,255,.5);text-align:center">
    <svg width="22" height="18" viewBox="0 0 22 18" style="margin-top:8px"><path d="M2 6c0-4 18-4 18 0l-1 2-4-1V5c-2-1-6-1-8 0v2L3 8z" fill="#fff"/><path d="M6 9h10l3 7H3z" fill="#fff"/><circle cx="11" cy="12.5" r="2" fill="#e4662c"/></svg>
  </span>
  <span style="padding-left:6px">CALL TO ACTION</span>
</div>

<footer class="abs footer">
  <div class="abs follow">Follow Us on</div>
  <span class="abs social" style="left:154px;background:#3b5b99"></span>
  <span class="abs social" style="left:186px;background:#3aa7dc"></span>
  <span class="abs social" style="left:219px;background:#1a73a8"></span>
  <span class="abs social" style="left:252px;background:#e8792a"></span>
  <div class="abs legal">Sitemap &nbsp;|&nbsp; Terms &nbsp;|&nbsp; Privacy<br>Copyrights @ 2013 &nbsp;All Rights Reserved</div>
  <div class="abs links">HOME &nbsp;|&nbsp; SOLUTIONS &nbsp;&nbsp;|&nbsp; SERVICES &nbsp;|&nbsp; SUPPORT &nbsp;|&nbsp; PARTNERS &nbsp;|&nbsp; ABOUT &nbsp;|&nbsp; DOWNLOAD</div>
  <div class="abs badges">
    <svg width="246" height="65" viewBox="0 0 246 65">
      <rect x="8" y="10" width="88" height="48" rx="3" fill="#e9eef3" stroke="#9aa7b2"/>
      <rect x="112" y="16" width="92" height="42" fill="#1c1c1c"/>
      <rect x="216" y="20" width="24" height="24" fill="#2a4fa0"/>
    </svg>
  </div>
</footer>

</body>
</html>
```